Brindlewave Systems Website Project

We require a design to revamp and existing website for a company that provides online solutions for small the medium sized businesses including web development, online marketing, social media, online business plans, social media and e-commerce. We are looking to use colours that integrate well with the current logo. Our target market are small to medium sized businesses and individuals looking for a trusted adviser to cover all their online services.
Existing website - www.brindlewavesystems.com.au
Updates
Participation payments added.
Storyboard layout mentioned in brief was not attached in error. It will be uploaded shortly.
Storyboard file added.
Target Market(s)
Revamp of existing website - Looking for a professional design in line with the target market of small to medium businesses
Industry/Entity Type
Business
Requirements
Must have
- Refer the attached storyboard layout for the site design and requirements. Basic header, footer and sidebar are to be the same on every page with the content changing to match the requirements on each page. 8 pages in total
Should not have
- No click here text

```html
<!DOCTYPE html>
<html lang="en">
<head>
<meta charset="utf-8">
<title>Brindlewave Systems</title>
<link href="https://fonts.googleapis.com/css2?family=Roboto+Condensed:wght@300;400&family=Arimo:wght@400;700&display=swap" rel="stylesheet">
<style>
:root{
  --green:#3a9b0f;
  --green-dark:#23780a;
  --green-light:#5cc12a;
  --text:#555;
  --muted:#777;
  --heading-green:#3c8f1c;
  --blue:#2fb6e6;
  --bar:#6f6f6f;
  --footer:#2b2b2b;
  --footer-text:#b8b8b8;
  --line:#d6d6d6;
}
*{box-sizing:border-box;margin:0;padding:0}
html,body{width:1200px;height:1154px;overflow:hidden;background:#fff}
body{position:relative;font-family:Arimo,Arial,sans-serif;color:var(--text)}
.abs{position:absolute}

/* header */
.brand{left:131px;top:10px}
.brand-mark{width:60px;height:60px;border-radius:50%;background:var(--green-light)}
.brand-name{left:131px;top:78px;font-family:"Roboto Condensed",sans-serif;font-weight:400;font-size:27px;line-height:28px;color:#3a3a3a;letter-spacing:1px}
.contact-info{right:131px;top:34px;text-align:right;font-family:"Roboto Condensed",sans-serif;font-weight:300;font-size:14px;line-height:22px;color:#444}
.follow{right:131px;top:105px;display:flex;align-items:center;gap:6px;font-family:"Roboto Condensed",sans-serif;font-size:16px;color:#222}
.follow span{margin-right:6px}
.dot{width:20px;height:20px;border-radius:50%;display:inline-block}

/* nav */
.nav{left:0;top:137px;width:1200px;height:47px;background:linear-gradient(#4fae19,var(--green-dark))}
.nav ul{position:absolute;left:131px;top:0;list-style:none;display:flex;height:47px}
.nav li{font-family:"Roboto Condensed",sans-serif;font-size:16px;color:#fff;line-height:47px;padding:0 30px;border-right:1px solid rgba(0,0,0,.18)}
.nav li:first-child{padding-left:27px;padding-right:28px}
.nav li:last-child{border:none}

/* hero */
.hero{left:131px;top:193px;width:685px;height:285px;border:2px solid var(--green-dark);border-radius:4px;overflow:hidden}
.hero-art{position:absolute;inset:0;background:radial-gradient(ellipse at 85% 40%,#3f9c1c 0%,#1d5e10 35%,#0f3209 70%,#0b2407 100%)}
.hero h1{position:absolute;left:30px;top:40px;font-family:"Roboto Condensed",sans-serif;font-weight:300;font-size:29px;color:#fff}
.hero p{position:absolute;left:32px;top:112px;font-family:"Roboto Condensed",sans-serif;font-weight:300;color:#fff;font-size:17px;line-height:32px}
.hero p b{font-weight:300;font-size:24px}

/* services */
.service{width:330px}
.service h2{font-family:"Roboto Condensed",sans-serif;font-weight:300;font-size:20px;color:var(--heading-green);margin-bottom:8px}
.service p{font-size:11px;line-height:18.7px;color:var(--text)}
.read-more{font-family:"Roboto Condensed",sans-serif;font-size:11.5px;color:#777;margin-top:10px;letter-spacing:.3px}

.bubble{width:103px;height:103px;border-radius:50%;background:linear-gradient(#4fd4f8,#14a8dc);border:3px solid #e8e8e8;color:#fff;font-family:"Roboto Condensed",sans-serif;font-weight:300;font-size:18px;line-height:18px;display:flex;align-items:center;justify-content:center;text-align:center;z-index:2}
.bubble.small{font-size:17px;line-height:17px}

/* sidebar */
.side-h{font-family:"Roboto Condensed",sans-serif;font-weight:300;font-size:20px;color:var(--heading-green)}
.field{left:836px;width:232px;height:28px;border:2px solid #ddd;border-radius:14px;font-size:11px;color:#888;padding:6px 8px;background:#fff}
.field.msg{height:83px;border-radius:12px}
.submit{left:836px;top:414px;width:74px;height:28px;border-radius:14px;background:linear-gradient(#4fae19,var(--green-dark));color:#fff;font-family:"Roboto Condensed",sans-serif;font-size:14px;text-align:center;line-height:28px}
.tweets{left:834px;top:498px;width:235px;height:224px;border:1px solid #ddd;padding:10px 10px;box-shadow:0 6px 6px -4px #999}
.tweet{font-size:11px;line-height:19px;color:#444;margin-bottom:12px}
.tweet small{display:block;color:#999;font-size:11px}
.community{left:834px;top:734px;font-family:Arimo,sans-serif;font-weight:700;font-size:18px;color:#3b5998}
.like{left:834px;top:764px;width:44px;height:21px;border:1px solid #c6cde0;background:#eef0f6;border-radius:2px;font-size:10px;color:#3b5998;text-align:center;line-height:19px}
.like-count{left:886px;top:771px;font-size:11px;color:#333}
.svc-bar{left:835px;width:232px;height:28px;background:var(--bar);color:#fff;font-size:11.5px;line-height:28px;padding-left:9px;clip-path:polygon(0 0,93% 0,100% 50%,93% 100%,0 100%)}
.svc-bar svg{position:absolute;right:20px;top:9px}

/* footer */
.footer{left:0;top:920px;width:1200px;height:234px;background:linear-gradient(#303030,#232323)}
.f-links{list-style:none;font-size:11.5px;line-height:21.5px;color:var(--footer-text)}
.f-div{top:960px;width:1px;height:142px;background:#555}
.f-h{font-family:"Roboto Condensed",sans-serif;font-weight:300;font-size:17px;color:#ccc}
.blog-title{font-size:12.5px;color:#ddd}
.blog-text{font-size:11px;line-height:17px;color:#8a8a8a;width:220px}
.more{font-size:11.5px;color:#4ab8e8}
.copy{left:131px;top:1117px;font-size:11.5px;color:#999}
</style>
</head>
<body>

<header>
  <div class="abs brand"><div class="brand-mark"></div></div>
  <div class="abs brand-name">BRINDLEWAVE<br>SYSTEMS</div>
  <div class="abs contact-info">Call us : 0400 118 362<br>Email: contact@brindlewavesystems.com.au</div>
  <div class="abs follow"><span>Follow us on</span><i class="dot" style="background:#3ab0e6"></i><i class="dot" style="background:#3b5998"></i></div>
</header>

<nav class="abs nav">
  <ul><li>Home</li><li>About us</li><li>Services</li><li>Portfolio</li><li>Contact us</li></ul>
</nav>

<section class="abs hero">
  <div class="hero-art" role="img" aria-label="Banner photo of a glowing green light bulb with radiating light rays"></div>
  <h1>Do you have &nbsp;an online business idea?</h1>
  <p><b>TALK US TODAY</b> to gain advice, support<br>and solutions to get it off the ground</p>
</section>

<article class="abs service" style="left:131px;top:497px">
  <h2>Web Development</h2>
  <p>A website represents the face of your business and it is critical to ensure your website can attract, retain and encourage visitors. At Brindlewave Systems we work with you to tailor a solution to your business requirements.</p>
  <div class="read-more">READ MORE →</div>
</article>
<article class="abs service" style="left:487px;top:497px">
  <h2>E-commerce</h2>
  <p>If you are looking at stepping into e-commerce leveraging off your existing business or establishing a purely online digital store we have a variety of tools available to tailor a solution to your needs. All e-commerce solutions...</p>
  <div class="read-more">READ MORE →</div>
</article>
<article class="abs service" style="left:131px;top:672px">
  <h2>Online Business</h2>
  <p>It takes time, effort and knowledge to develop an online business. Whether adapting your bricks and mortar business to the online environment or establishing a purely online business it is important to get the right advice...</p>
  <div class="read-more">READ MORE →</div>
</article>
<article class="abs service" style="left:487px;top:672px">
  <h2>Online Marketing</h2>
  <p>Why have a website and an online presence without an effective online marketing strategy? At Brindlewave Systems we understand that a website is only one online tool that can be used to drive business success...</p>
  <div class="read-more">READ MORE →</div>
</article>

<div class="abs bubble" style="left:131px;top:838px">Our Works</div>
<div class="abs bubble small" style="left:256px;top:838px">Why Choose<br>us</div>

<aside>
  <div class="abs side-h" style="left:835px;top:192px">Quick Contact</div>
  <div class="abs field" style="top:227px">name</div>
  <div class="abs field" style="top:260px">email id</div>
  <div class="abs field" style="top:293px">phone number</div>
  <div class="abs field msg" style="top:325px">message</div>
  <div class="abs submit">SUBMIT</div>

  <div class="abs side-h" style="left:834px;top:465px">Latest Tweets</div>
  <div class="abs tweets">
    <div class="tweet">@marenwhitby Chirper fail last night sorry. Thought you were...<small>3 hrs ago</small></div>
    <div class="tweet">@marenwhitby Chirper fail last night sorry. Thought you were...<small>3 hrs ago</small></div>
    <div class="tweet">@marenwhitby Chirper fail last night sorry. Thought you were...<small>3 hrs ago</small></div>
  </div>

  <div class="abs community">Community</div>
  <div class="abs like">Like</div>
  <div class="abs like-count">100 people like this</div>

  <div class="abs svc-bar" style="top:806px">Services one<svg width="10" height="10" viewBox="0 0 10 10"><path d="M1 1l4 4-4 4M5 1l4 4-4 4" stroke="#fff" fill="none" stroke-width="1.4"/></svg></div>
  <div class="abs svc-bar" style="top:836px">Services two<svg width="10" height="10" viewBox="0 0 10 10"><path d="M1 1l4 4-4 4M5 1l4 4-4 4" stroke="#fff" fill="none" stroke-width="1.4"/></svg></div>
  <div class="abs svc-bar" style="top:866px">Services three<svg width="10" height="10" viewBox="0 0 10 10"><path d="M1 1l4 4-4 4M5 1l4 4-4 4" stroke="#fff" fill="none" stroke-width="1.4"/></svg></div>
</aside>

<footer>
  <div class="abs footer"></div>
  <ul class="abs f-links" style="left:132px;top:958px"><li>Home</li><li>About us</li><li>Blogs</li><li>Contact us</li></ul>
  <div class="abs f-div" style="left:306px"></div>
  <ul class="abs f-links" style="left:334px;top:958px"><li>Web Design and Development</li><li>Search Engine Optimisation</li><li>Online Business Consultants</li><li>Online Marketing</li><li>Social Media</li><li>E-commerce</li></ul>
  <div class="abs f-div" style="left:543px"></div>
  <div class="abs f-h" style="left:567px;top:958px">Blog Posts</div>
  <div class="abs blog-title" style="left:567px;top:993px">The 8 steps of an Advertising campaign</div>
  <div class="abs blog-text" style="left:567px;top:1015px">In the past, I worked with a business that made its decisions on where to advertise based entirely on ...</div>
  <div class="abs more" style="left:567px;top:1071px">more...</div>
  <div class="abs f-div" style="left:802px"></div>
  <div class="abs f-h" style="left:820px;top:964px">Follow us on</div>
  <i class="abs dot" style="left:925px;top:962px;width:22px;height:22px;background:#3ab0e6"></i>
  <i class="abs dot" style="left:954px;top:962px;width:22px;height:22px;background:#3b8fd8"></i>
  <div class="abs more" style="left:957px;top:1054px">x31</div>
  <div class="abs copy">© All Rights Reserved Brindlewave Systems 2012</div>
</footer>

</body>
</html>
```